Verpackungsetikett für Softeisbecher
Zielgruppe
Wir produzieren Speiseeis, füllen dieses in entsprechende Verpackungseinheiten ab und vermarkten es. Zielgruppe sind alle die, die Eis mögen.
Aufgabenstellung
Das bestehende Etikettendesign (rund 8cm Durchmesser) soll neu überarbeitet werden. Dazu soll es mit unserem neuen Logo (Anhang) versehen werden. Wir freuen uns über fotolose Vorschläge bzw. Design´s mit Foto. Alle Angaben über z.B. Inhaltstoffe, Herstellungdatum, Aufbewahrungtemperatur, Barcode u.s.w.kommen auf ein separates Etikett am Boden des Bechers.Das Erscheinungsbild des Etiketts sollte eine gewisse Neutralität haben, so dass es für die verschiedensten Geschmacksrichtungen verwendet werden kann, sprich ein Etikett für alle Eissorten. Nur der Name der Geschmacksrichtung unterscheidet die Etiketten. Wir verweisen auf einige Link`s ,auf denen man Etikettenbeispiele (z. B. Frischkäse) sieht, die unseren Vorstellungen der Gestaltung entsprechen. Vielen Dank im Voraus

```html
<!DOCTYPE html>
<html lang="de">
<head>
<meta charset="utf-8">
<title>Softeis Deckeletikett – Heidelbeer Joghurt</title>
<link rel="stylesheet" href="https://fonts.googleapis.com/css2?family=Pacifico&family=Courgette&family=Nunito:wght@800&display=swap">
<style>
  :root {
    --canvas: #ffffff;
    --ring-blue: #1a8fd0;
    --ring-blue-light: #5cc0ee;
    --ring-purple: #6a5a8c;
    --ring-purple-light: #8f7fae;
    --splash-white: #f7fbfd;
    --splash-blue: #d9ecf6;
    --splash-green: #d6e8b4;
    --brand-ink: #2f6fb0;
    --subline: #6b86a3;
    --title-blue: #1b5aa6;
    --ribbon-orange: #e39a2a;
    --ribbon-orange-dark: #b9701a;
    --ribbon-purple: #5f4e83;
    --berry-blue: #4a5f94;
    --berry-leaf: #6fa55a;
  }
  html, body {
    margin: 0;
    width: 1200px;
    height: 1200px;
    overflow: hidden;
    background: var(--canvas);
  }
  .label {
    display: block;
    width: 1200px;
    height: 1200px;
  }
  .brand-name {
    font-family: "Nunito", sans-serif;
    font-weight: 800;
    font-size: 72px;
    fill: var(--brand-ink);
  }
  .brand-subline {
    font-family: "Nunito", sans-serif;
    font-weight: 800;
    font-size: 26px;
    letter-spacing: 1px;
    fill: var(--subline);
  }
  .product-title {
    font-family: "Pacifico", cursive;
    font-size: 190px;
    fill: var(--title-blue);
    stroke: #ffffff;
    stroke-width: 14px;
    paint-order: stroke fill;
    stroke-linejoin: round;
  }
  .ribbon-claim {
    font-family: "Courgette", cursive;
    font-size: 50px;
    fill: #ffffff;
  }
  .ribbon-flavour {
    font-family: "Courgette", cursive;
    font-size: 38px;
    fill: #ffffff;
  }
</style>
</head>
<body>
<svg class="label" viewBox="0 0 1200 1200" xmlns="http://www.w3.org/2000/svg">
  <defs>
    <clipPath id="label-shape"><circle cx="600" cy="600" r="500"/></clipPath>
    <linearGradient id="ring-blue-grad" x1="0" y1="0" x2="1" y2="1">
      <stop offset="0" stop-color="var(--ring-blue-light)"/>
      <stop offset="1" stop-color="var(--ring-blue)"/>
    </linearGradient>
    <linearGradient id="ring-purple-grad" x1="0" y1="0" x2="1" y2="0">
      <stop offset="0" stop-color="var(--ring-purple)"/>
      <stop offset="1" stop-color="var(--ring-purple-light)"/>
    </linearGradient>
    <radialGradient id="splash-grad" cx="0.4" cy="0.55" r="0.7">
      <stop offset="0" stop-color="var(--splash-white)"/>
      <stop offset="0.6" stop-color="#ffffff"/>
      <stop offset="1" stop-color="var(--splash-blue)"/>
    </radialGradient>
    <linearGradient id="splash-green-grad" x1="1" y1="0" x2="0.3" y2="0.6">
      <stop offset="0" stop-color="var(--splash-green)"/>
      <stop offset="1" stop-color="var(--splash-green)" stop-opacity="0"/>
    </linearGradient>
    <linearGradient id="claim-grad" x1="0" y1="0" x2="1" y2="0">
      <stop offset="0" stop-color="var(--ribbon-orange-dark)"/>
      <stop offset="0.5" stop-color="var(--ribbon-orange)"/>
      <stop offset="1" stop-color="#f0c060"/>
    </linearGradient>
    <radialGradient id="berry-grad" cx="0.45" cy="0.45" r="0.6">
      <stop offset="0" stop-color="var(--berry-blue)"/>
      <stop offset="0.75" stop-color="#34477a"/>
      <stop offset="1" stop-color="var(--berry-leaf)" stop-opacity="0.6"/>
    </radialGradient>
  </defs>

  <g class="label-disc" clip-path="url(#label-shape)">
    <rect class="ring-blue" x="100" y="100" width="1000" height="1000" fill="url(#ring-blue-grad)"/>
    <path class="ring-purple" d="M100 840 Q600 1010 1100 690 L1100 1100 L100 1100 Z" fill="url(#ring-purple-grad)"/>
    <path class="ring-highlight" d="M160 420 Q520 80 1020 300" fill="none" stroke="#ffffff" stroke-opacity="0.45" stroke-width="26"/>

    <g role="img" aria-label="Milchspritzer in Weiß mit zartem Blau- und Grünschimmer">
      <circle class="splash-field" cx="600" cy="575" r="445" fill="url(#splash-grad)"/>
      <circle class="splash-tint" cx="600" cy="575" r="445" fill="url(#splash-green-grad)"/>
    </g>
  </g>

  <g class="brand">
    <circle class="brand-dot" cx="468" cy="346" r="20" fill="var(--brand-ink)"/>
    <text class="brand-name" x="622" y="372" text-anchor="middle">Alvora</text>
    <text class="brand-subline" x="600" y="422" text-anchor="middle">frisch gerührt!</text>
  </g>

  <text class="product-title" x="600" y="680" text-anchor="middle">Softeis</text>

  <g class="ribbons" clip-path="url(#label-shape)">
    <polygon class="ribbon-claim-band" points="100,796 712,758 712,826 100,864" fill="url(#claim-grad)"/>
    <text class="ribbon-claim" x="196" y="826" transform="rotate(-3.5 196 826)">mmh… so lecker!</text>
    <polygon class="ribbon-flavour-band" points="100,874 664,842 664,902 100,934" fill="var(--ribbon-purple)"/>
    <text class="ribbon-flavour" x="204" y="904" transform="rotate(-3.2 204 904)">Heidelbeer Joghurt</text>
  </g>

  <ellipse class="flavour-visual" cx="790" cy="872" rx="165" ry="108" fill="url(#berry-grad)" role="img" aria-label="Heidelbeeren mit grünen Blättern"/>
</svg>
</body>
</html>
```